Symposium Flyer

I need a flyer for advertising an upcoming symposium titled, "Stirring and settling the chromatin code", I am organizing as well as a webpage design for the symposium. The Symposium is taking place on Thursday, February 7th, 2019 at the Valdmere University Harrowgate School of Medicine. It is being held by the Gene Regulation Centre at the Corvath Hall for Applied Discovery (Maplewick Auditorium and Lobby, 1275 Larkspur Terrace Way, Philadelphia, PA 19187). You can view previous symposiums from our institution at https://events.valdmere-med.example/generegulation/symposiums/

Our Keynote speakers for this symposium are:
Theodor Wallmark, M.D., Professor of Biology at the Ostrander Polytechnic Academy; Founding Member of the Brackenfield Foundation for Life Science Study; Member of the Council of Clinical Scholars.
AND
Martin (Marty) Okafor, M.D., President of the Quelvora Laboratories for Therapeutic Discovery (QLTD)

We will be adding 8 more speakers to this event, so please leave room for extra speakers to be added and for a website registration link and QR code to be added.

Please email me should have additional questions - torvik@mail.valdmere-med.example

```html
<!DOCTYPE html>
<html lang="en">
<head>
<meta charset="utf-8">
<title>Stirring and settling the chromatin code — Symposium 2019</title>
<link rel="stylesheet" href="https://fonts.googleapis.com/css2?family=Open+Sans:wght@300;400;700&family=Tinos&display=swap">
<style>
  :root {
    --band-green: #c3dea7;
    --heading-green: #6d9b2c;
    --title-red: #cb1118;
    --ink: #1d1d1d;
    --white: #ffffff;
    --helix-green: #9fd25a;
    --helix-gold: #e6a521;
    --helix-teal: #86b9b4;
  }
  html, body { margin: 0; padding: 0; overflow: hidden; background: var(--white); }
  .flyer {
    position: relative; width: 848px; height: 1200px; overflow: hidden;
    background: var(--white); font-family: "Open Sans", Arial, sans-serif; color: var(--ink);
  }
  .date-band { position: absolute; left: 0; top: 0; width: 848px; height: 462px; background: var(--band-green); }
  .year-outline { position: absolute; left: 0; top: 0; width: 848px; height: 300px; }
  .helix-art { position: absolute; left: 0; top: 0; width: 848px; height: 1200px; }
  .event-date {
    position: absolute; left: 112px; top: 180px; margin: 0;
    font-weight: 700; font-size: 64px; line-height: 1; color: var(--white); letter-spacing: -1px;
  }
  .event-title {
    position: absolute; left: 44px; top: 284px; margin: 0;
    color: var(--title-red); font-weight: 700; font-size: 58px; line-height: 52px; letter-spacing: -1.5px;
  }
  .event-title .minor { font-weight: 300; font-size: 36px; letter-spacing: 0; }
  .section-heading { margin: 0; color: var(--heading-green); font-weight: 700; font-size: 29px; line-height: 30px; }
  .keynotes { position: absolute; right: 512px; top: 550px; width: 320px; text-align: right; }
  .keynote { margin-top: 20px; }
  .speaker-name { margin: 0; font-weight: 700; font-size: 18px; line-height: 24px; }
  .speaker-role { margin: 4px 0 0; font-family: "Tinos", "Times New Roman", serif; font-size: 14.5px; line-height: 17px; }
  .keynote .speaker-role + .speaker-role { margin-top: 4px; }
  .venue { position: absolute; right: 512px; top: 886px; width: 320px; text-align: right; }
  .venue-address { margin: 10px 0 0; font-family: "Tinos", "Times New Roman", serif; font-size: 15px; line-height: 20px; }
  .speakers { position: absolute; left: 368px; top: 508px; width: 300px; }
  .speakers .section-heading { font-size: 31px; margin-bottom: 12px; }
  .speaker { height: 73.5px; }
  .speaker .speaker-role { margin-top: 2px; line-height: 15.5px; }
  .organisers { position: absolute; left: 44px; top: 1046px; display: flex; gap: 22px; align-items: center; }
  .organiser { display: flex; align-items: center; gap: 8px; font-weight: 700; font-size: 12px; line-height: 14px; color: #1f3f8f; }
  .organiser-mark { width: 18px; height: 18px; background: #1f3f8f; flex: none; }
  .organiser-mark.round { border-radius: 50%; background: #c8102e; }
  .organiser.centre { color: #c8102e; }
</style>
</head>
<body>
<main class="flyer">
  <div class="date-band"></div>

  <svg class="year-outline" viewBox="0 0 848 300" aria-hidden="true">
    <text x="165" y="248" font-family="Open Sans, Arial, sans-serif" font-weight="300" font-size="300"
          fill="none" stroke="#ffffff" stroke-width="1.5" letter-spacing="-6">2019</text>
  </svg>

  <svg class="helix-art" viewBox="0 0 848 1200" role="img"
       aria-label="Illustration of a golden DNA double helix coiled around green histone proteins">
    <defs>
      <linearGradient id="helixTones" x1="0" y1="0" x2="0.3" y2="1">
        <stop offset="0" stop-color="#9fd25a"/>
        <stop offset="0.35" stop-color="#e6a521"/>
        <stop offset="0.7" stop-color="#86b9b4"/>
        <stop offset="1" stop-color="#e6a521"/>
      </linearGradient>
    </defs>
    <path d="M480 70 L848 70 L848 1200 L640 1200 C650 1000 700 800 640 640 C600 545 525 505 475 470 C450 380 450 160 480 70 Z"
          fill="url(#helixTones)" opacity="0.85"/>
  </svg>

  <p class="event-date">7th Feb</p>

  <h1 class="event-title">
    Stirring<span class="minor">and</span><br>
    Settling<br>
    <span class="minor">the</span>Chromatin Code
  </h1>

  <section class="keynotes">
    <h2 class="section-heading">Keynote<br>speakers</h2>
    <div class="keynote">
      <p class="speaker-name">Theodor Wallmark, M.D.</p>
      <p class="speaker-role">Professor of Biology at the Ostrander Polytechnic Academy,</p>
      <p class="speaker-role">Founding Member of the Brackenfield Foundation for Life Science Study,</p>
      <p class="speaker-role">Member of the Council of Clinical Scholars.</p>
    </div>
    <div class="keynote">
      <p class="speaker-name">Martin (Marty) Okafor, M.D</p>
      <p class="speaker-role">President of the Quelvora Laboratories for Therapeutic Discovery</p>
    </div>
  </section>

  <section class="venue">
    <h2 class="section-heading">Venue</h2>
    <p class="venue-address">Maplewick Auditorium and Lobby, 1275 Larkspur Terrace Way,<br>Philadelphia,<br>PA 19187</p>
  </section>

  <section class="speakers">
    <h2 class="section-heading">Speakers</h2>
    <div class="speaker">
      <p class="speaker-name">Theodor Wallmark, M.D.</p>
      <p class="speaker-role">Professor of Biology<br>Ostrander Polytechnic Academy</p>
    </div>
    <div class="speaker">
      <p class="speaker-name">Martin (Marty) Okafor, M.D</p>
      <p class="speaker-role">President<br>Quelvora Laboratories for Therapeutic<br>Ostrander Polytechnic Academy</p>
    </div>
    <div class="speaker">
      <p class="speaker-name">Theodor Wallmark, M.D.</p>
      <p class="speaker-role">Professor of Biology<br>Ostrander Polytechnic Academy</p>
    </div>
    <div class="speaker">
      <p class="speaker-name">Martin (Marty) Okafor, M.D</p>
      <p class="speaker-role">President<br>Quelvora Laboratories for Therapeutic<br>Ostrander Polytechnic Academy</p>
    </div>
    <div class="speaker">
      <p class="speaker-name">Theodor Wallmark, M.D.</p>
      <p class="speaker-role">Professor of Biology<br>Ostrander Polytechnic Academy</p>
    </div>
    <div class="speaker">
      <p class="speaker-name">Martin (Marty) Okafor, M.D</p>
      <p class="speaker-role">President<br>Quelvora Laboratories for Therapeutic<br>Ostrander Polytechnic Academy</p>
    </div>
    <div class="speaker">
      <p class="speaker-name">Theodor Wallmark, M.D.</p>
      <p class="speaker-role">Professor of Biology<br>Ostrander Polytechnic Academy</p>
    </div>
    <div class="speaker">
      <p class="speaker-name">Martin (Marty) Okafor, M.D</p>
      <p class="speaker-role">President<br>Quelvora Laboratories for Therapeutic<br>Ostrander Polytechnic Academy</p>
    </div>
  </section>

  <footer class="organisers">
    <div class="organiser"><span class="organiser-mark"></span><span>Valdmere University<br>Harrowgate School<br>of Medicine</span></div>
    <div class="organiser centre"><span class="organiser-mark round"></span><span>Gene Regulation<br>Centre</span></div>
  </footer>
</main>
</body>
</html>
```